Slick Quillnest Ad

We've recently re-branded our business to reflect our ethos "Wealth is about more than money - it's about choice." We aim to protect your hard-earned success and help achieve your lifestyle aspirations, whether that's retiring at fifty to go globetrotting, or buying your first home. We're a financial consultancy that primarily services high-net-worth clients.

Our brand is minimalist, modern (check out our website) and the brief focuses on our strong investment return for the past 12 years.

Task: The attached brief is for a Quillnest advertisement. Please see competitor images as a guide to how 'returns' and 'branding' can both be displayed in a design.

Target Market(s)

+30

Font styles to use
Sans Serif

Requirements
Must have
• Creative should feature the strong investment return, and design aesthetic should be 'on-brand' (modern, minimalist, lifestyle focused).

```html
<!DOCTYPE html>
<html lang="en">
<head>
<meta charset="utf-8">
<title>Quillnest – Investment Returns Ad</title>
<link href="https://fonts.googleapis.com/css2?family=Poppins:wght@400;600&display=swap" rel="stylesheet">
<style>
  :root {
    --lime: #abbe08;
    --lime-light: #b8c71c;
    --lime-deep: #97ab02;
    --map-tone: #9cb004;
    --ink: #3b403c;
    --white: #ffffff;
    --rule: #6f7a3a;
    --ring: #8a8f86;
    --cake-dark: #3a2118;
    --cake-mid: #5e3826;
    --cake-light: #86593d;
  }
  * { margin: 0; padding: 0; box-sizing: border-box; }
  html, body { width: 1200px; height: 688px; overflow: hidden; }
  body { font-family: "Poppins", sans-serif; }

  .ad {
    position: relative;
    width: 1200px;
    height: 688px;
    overflow: hidden;
    background: radial-gradient(ellipse at 55% 45%, var(--lime-light) 0%, var(--lime) 55%, var(--lime-deep) 100%);
  }

  .world-map {
    position: absolute;
    left: 210px; top: 80px;
    width: 900px; height: 500px;
    border-radius: 40%;
    background: radial-gradient(ellipse at center, var(--map-tone) 0%, rgba(156,176,4,0) 70%);
    opacity: 0.7;
  }

  .brand-disc {
    position: absolute;
    left: 38px; top: -148px;
    width: 304px; height: 304px;
    border-radius: 50%;
    background: var(--white);
    box-shadow: 0 0 0 3px var(--ring);
  }
  .brand-name {
    position: absolute;
    left: 38px; top: 62px;
    width: 304px;
    text-align: center;
    font-weight: 600;
    font-size: 30px;
    color: var(--lime-deep);
  }

  .headline {
    position: absolute;
    left: 84px; top: 216px;
    font-weight: 600;
    font-size: 47px;
    line-height: 56.6px;
    color: var(--ink);
    letter-spacing: -0.5px;
  }
  .headline .figure { color: var(--white); }

  .dessert-photo {
    position: absolute;
    left: 648px; top: 40px;
    width: 500px; height: 550px;
    border-radius: 24px;
    background: linear-gradient(180deg, var(--cake-dark) 0%, var(--cake-mid) 45%, var(--cake-light) 65%, var(--cake-dark) 100%);
  }

  .footer-rule {
    position: absolute;
    left: 84px; top: 645px;
    width: 765px; height: 1px;
    background: var(--rule);
  }
  .web-address {
    position: absolute;
    left: 878px; top: 624px;
    font-weight: 400;
    font-size: 22px;
    color: var(--white);
  }
</style>
</head>
<body>
  <main class="ad">
    <div class="world-map" role="img" aria-label="Faint world map in the background"></div>

    <div class="brand-disc"></div>
    <div class="brand-name">Quillnest</div>

    <h1 class="headline">
      Our global<br>
      investment portfolio<br>
      delivered<br>
      <span class="figure">20.5% returns</span><br>
      over the<br>
      past 12 months.
    </h1>

    <div class="dessert-photo" role="img" aria-label="Photo of a slice of layered chocolate mousse cake topped with a cherry, cream and mint"></div>

    <div class="footer-rule"></div>
    <p class="web-address">www.quillnest.com</p>
  </main>
</body>
</html>
```